Business Card Design Project

Hello
I want a Simple Business card that uses the company logo that is easily reasonable but looks professional as I am an IT Services company and would look to share these cards with prospective clients.
The details are:
Kestrel Arc Solutions
14 Morrow Lane
Birmingham
B7 4QX
Telephone 0845 217 6640
I would like my name Oliver Hastings and my title Director on the card.
Target Market(s)
IT Professionals
Industry/Entity Type
Business

```html
<!DOCTYPE html>
<html lang="en">
<head>
<meta charset="utf-8">
<title>Kestrel Arc Solutions – Business Card</title>
<link rel="stylesheet" href="https://fonts.googleapis.com/css2?family=Open+Sans:wght@400;600&display=swap">
<style>
  :root {
    --stage: #e9e9e9;
    --card-light: #ffffff;
    --card-edge: #e4e4e4;
    --ink: #1f1f1f;
    --muted: #8c8c8c;
    --leaf: #5aa93b;
    --leaf-soft: #b9dba1;
    --sun-soft: #f4f2c4;
    --divider: #9a9a9a;
  }
  * { box-sizing: border-box; margin: 0; padding: 0; }
  html, body {
    width: 1200px;
    height: 451px;
    overflow: hidden;
    background: var(--stage);
    font-family: "Open Sans", Arial, sans-serif;
  }
  .card {
    position: absolute;
    left: 210px;
    top: 5px;
    width: 780px;
    height: 440px;
    overflow: hidden;
    background: radial-gradient(ellipse at 50% 40%, var(--card-light) 45%, var(--card-edge) 100%);
  }
  .card-footer-tint {
    position: absolute;
    left: 0;
    bottom: 0;
    width: 100%;
    height: 120px;
    background: linear-gradient(to bottom, rgba(244, 242, 196, 0) 0%, var(--sun-soft) 40%, var(--leaf-soft) 100%);
  }
  .brand {
    position: absolute;
    left: 0;
    width: 403px;
    top: 238px;
    display: flex;
    align-items: center;
    justify-content: center;
    gap: 12px;
  }
  .brand-dot {
    width: 38px;
    height: 38px;
    border-radius: 50%;
    background: var(--leaf);
  }
  .brand-name {
    font-size: 42px;
    font-weight: 600;
    color: var(--ink);
    letter-spacing: -0.5px;
    line-height: 1;
  }
  .divider {
    position: absolute;
    left: 403px;
    top: 62px;
    width: 1px;
    height: 338px;
    background: linear-gradient(to bottom, transparent, var(--divider) 10%, var(--divider) 85%, transparent);
  }
  .contact {
    position: absolute;
    left: 471px;
    top: 108px;
    width: 290px;
  }
  .contact-name {
    width: 250px;
    text-align: center;
    font-size: 25px;
    color: var(--leaf);
    letter-spacing: 1.5px;
    line-height: 30px;
  }
  .contact-title {
    width: 250px;
    text-align: center;
    font-size: 20px;
    color: var(--muted);
    letter-spacing: 1.5px;
    line-height: 28px;
    margin-bottom: 12px;
  }
  .address {
    list-style: none;
    font-size: 21px;
    color: var(--ink);
    letter-spacing: 1.5px;
    line-height: 30px;
  }
  .phone {
    display: flex;
    align-items: center;
    gap: 8px;
    margin-top: 4px;
    font-size: 21px;
    color: var(--ink);
    letter-spacing: 1.5px;
  }
  .phone-icon { width: 24px; height: 24px; }
</style>
</head>
<body>
  <div class="card">
    <div class="card-footer-tint" role="img" aria-label="Soft yellow and green decorative band along the bottom edge"></div>

    <div class="brand">
      <span class="brand-dot"></span>
      <span class="brand-name">Kestrel Arc</span>
    </div>

    <div class="divider"></div>

    <div class="contact">
      <p class="contact-name">Oliver Hastings</p>
      <p class="contact-title">Director</p>
      <ul class="address">
        <li>Kestrel Arc Solutions</li>
        <li>14 Morrow Lane</li>
        <li>Birmingham</li>
        <li>B7 4QX</li>
      </ul>
      <p class="phone">
        <svg class="phone-icon" viewBox="0 0 24 24" aria-hidden="true">
          <circle cx="12" cy="12" r="10.5" fill="none" stroke="#1f1f1f" stroke-width="1.6"/>
          <path d="M8.3 6.5c.5-.4 1.1-.3 1.4.2l1 1.7c.3.5.2 1-.2 1.3l-.7.5c.5 1.4 1.5 2.6 2.8 3.4l.6-.6c.4-.4 1-.4 1.4-.1l1.6 1.1c.5.3.6 1 .2 1.4l-.7.8c-.6.6-1.5.8-2.3.5-3-1.2-5.2-3.6-6.1-6.7-.2-.8 0-1.6.6-2.1z" fill="#1f1f1f"/>
        </svg>
        <span>0845 217 6640</span>
      </p>
    </div>
  </div>
</body>
</html>
```